Need a stunning looking Business Card Design for my Telecom Business, Wow FACTOR!

I deal with high level IT Directors , and Contractors.
I need to impress them with a sleek , professional and unique business card.
Im thinking options as far as rounded edges, plastic , or even metal card or die cut on a corner.
Whatever looks better and leave an unforgettable first impression.
im looking for the wow factor.
Front should have the basics info (attached on the picture of current business card)
i would like to add picture of myself somewhere
Back side
should have logo and maybe some pictures or past projects, you can download from my website ( www.lumvexholdings.com)

```html
<!DOCTYPE html>
<html lang="en">
<head>
<meta charset="UTF-8">
<title>Lumvex Holdings – Business Card</title>
<link href="https://fonts.googleapis.com/css2?family=Exo+2:wght@400;600;700&display=swap" rel="stylesheet">
<style>
  :root {
    --backdrop: #3a3b3e;
    --card-navy: #14284f;
    --card-navy-deep: #0f1f40;
    --ink-white: #ffffff;
    --ink-soft: #d7def0;
    --accent-red: #e2302b;
    --accent-orange: #f39c12;
    --accent-green: #7cc242;
    --accent-blue: #3aa6e8;
  }
  * { box-sizing: border-box; margin: 0; padding: 0; }
  html, body { width: 1200px; height: 801px; overflow: hidden; }
  body {
    background: var(--backdrop);
    font-family: "Exo 2", sans-serif;
    color: var(--ink-white);
    position: relative;
  }
  .card {
    position: absolute;
    width: 540px;
    height: 309px;
    border-radius: 18px;
    background: linear-gradient(135deg, var(--card-navy) 0%, var(--card-navy-deep) 100%);
    overflow: hidden;
  }
  .card--back { left: 40px; top: 246px; }
  .card--front { left: 620px; top: 246px; }

  .pattern-field {
    position: absolute; inset: 0;
    background: linear-gradient(160deg, rgba(40,70,130,0.35), rgba(15,31,64,0.1));
  }
  .brand {
    display: flex; align-items: center; gap: 10px;
    font-weight: 600; letter-spacing: 2px; text-transform: uppercase;
    color: var(--ink-white);
  }
  .brand__dot { width: 14px; height: 14px; border-radius: 50%; background: var(--accent-blue); }

  .back-content {
    position: absolute; inset: 0;
    display: flex; flex-direction: column; align-items: center; justify-content: center; gap: 18px;
  }
  .back-content .brand { font-size: 30px; }
  .website { font-size: 15px; letter-spacing: 1.5px; color: var(--ink-soft); }

  .card--front .brand { position: absolute; left: 34px; top: 40px; font-size: 22px; }

  .portrait {
    position: absolute; right: 40px; top: 22px;
    width: 118px; height: 118px; border-radius: 50%;
    background: linear-gradient(180deg, #5b4638 0%, #c9a38a 55%, #b7bcc4 100%);
  }
  .identity {
    position: absolute; right: 34px; top: 152px; text-align: right;
  }
  .identity__name { font-size: 21px; font-weight: 700; letter-spacing: 1px; text-transform: uppercase; }
  .identity__role { font-size: 12px; color: var(--ink-soft); margin-top: 2px; }
  .identity__trade { font-size: 12px; font-weight: 700; margin-top: 12px; }
  .identity__offices { font-size: 12px; color: var(--ink-soft); margin-top: 2px; }

  .contact-list {
    position: absolute; left: 34px; bottom: 30px; list-style: none;
    font-size: 14px; line-height: 1.5;
  }
  .contact-list li { display: flex; align-items: center; gap: 8px; }
  .contact-list strong { font-weight: 700; margin-left: 4px; }
  .contact-list svg { width: 14px; height: 14px; flex: none; }
</style>
</head>
<body>

<section class="card card--back" aria-label="Card back">
  <div class="pattern-field" role="img" aria-label="Faint repeating background pattern"></div>
  <div class="back-content">
    <div class="brand"><span class="brand__dot"></span>Lumvex Holdings</div>
    <p class="website">www.lumvexholdings.com</p>
  </div>
</section>

<section class="card card--front" aria-label="Card front">
  <div class="brand"><span class="brand__dot"></span>Lumvex Holdings</div>

  <div class="portrait" role="img" aria-label="Portrait photo of Dorian Kessler"></div>

  <div class="identity">
    <p class="identity__name">Dorian Kessler</p>
    <p class="identity__role">Operations Manager</p>
    <p class="identity__trade">Low Voltage Contractor</p>
    <p class="identity__offices">Offices in Miami, Broward and Palm Beach</p>
  </div>

  <ul class="contact-list">
    <li>
      <svg viewBox="0 0 24 24"><path fill="var(--accent-red)" d="M6.6 10.8a15 15 0 0 0 6.6 6.6l2.2-2.2c.3-.3.7-.4 1-.2 1.1.4 2.3.6 3.6.6.6 0 1 .4 1 1V20c0 .6-.4 1-1 1A17 17 0 0 1 3 4c0-.6.4-1 1-1h3.5c.6 0 1 .4 1 1 0 1.3.2 2.5.6 3.6.1.3 0 .7-.2 1z"/></svg>
      (305) 555-0142 <strong>Miami</strong>
    </li>
    <li>
      <svg viewBox="0 0 24 24"><path fill="var(--accent-orange)" d="M6.6 10.8a15 15 0 0 0 6.6 6.6l2.2-2.2c.3-.3.7-.4 1-.2 1.1.4 2.3.6 3.6.6.6 0 1 .4 1 1V20c0 .6-.4 1-1 1A17 17 0 0 1 3 4c0-.6.4-1 1-1h3.5c.6 0 1 .4 1 1 0 1.3.2 2.5.6 3.6.1.3 0 .7-.2 1z"/></svg>
      (954) 555-0187 <strong>Broward</strong>
    </li>
    <li>
      <svg viewBox="0 0 24 24"><path fill="var(--accent-green)" d="M6.6 10.8a15 15 0 0 0 6.6 6.6l2.2-2.2c.3-.3.7-.4 1-.2 1.1.4 2.3.6 3.6.6.6 0 1 .4 1 1V20c0 .6-.4 1-1 1A17 17 0 0 1 3 4c0-.6.4-1 1-1h3.5c.6 0 1 .4 1 1 0 1.3.2 2.5.6 3.6.1.3 0 .7-.2 1z"/></svg>
      (561) 555-0163 <strong>Palm Beach</strong>
    </li>
    <li>
      <svg viewBox="0 0 24 24"><path fill="var(--accent-blue)" d="M2 5h20v14H2z"/><path fill="none" stroke="var(--card-navy)" stroke-width="2" d="M2 5l10 8 10-8"/></svg>
      info@lumvexholdings.com
    </li>
  </ul>
</section>

</body>
</html>
```